IT Company looking to market towards Dental Offices

I am looking for a full-color design. Using my existing logo. Must have High Res stock photos. The brochure needs to be full page edge to edge design single fold pamphlet style. Content provided. Please see the website in attached Word Doc for more content.

```html
<!DOCTYPE html>
<html lang="en">
<head>
<meta charset="utf-8">
<title>Byte Harbor – Dental IT Brochure</title>
<link href="https://fonts.googleapis.com/css2?family=Open+Sans:wght@400;600;700;800&display=swap" rel="stylesheet">
<style>
  :root{
    --navy:#1b2c86;
    --sky:#1f86d6;
    --white:#ffffff;
    --stage:#e6e6e6;
    --photo-light:#d8d4cc;
    --photo-dark:#6d6a66;
  }
  *{margin:0;padding:0;box-sizing:border-box}
  html,body{width:900px;height:1200px;overflow:hidden;background:var(--stage);font-family:"Open Sans",sans-serif}
  .spread{position:absolute;left:20px;top:297px;width:860px;height:606px;background:var(--navy);overflow:hidden;color:var(--white);box-shadow:0 6px 18px rgba(0,0,0,.25)}
  .spread-art{position:absolute;left:0;top:0;width:860px;height:606px}
  .fold{position:absolute;left:430px;top:0;width:1px;height:100%;background:rgba(0,0,0,.12)}
  .brand-name{position:absolute;left:19px;top:322px;font-weight:700;font-size:21px;line-height:1.2;color:var(--white)}
  .section-title{font-weight:600;font-size:14px;line-height:1.3;position:relative;padding-bottom:3px;margin-bottom:8px}
  .section-title::after{content:"";position:absolute;left:0;bottom:0;width:22px;height:2px;background:var(--white)}
  .about{position:absolute;left:19px;top:382px;width:400px}
  .about p{font-size:8.4px;line-height:1.45;margin-bottom:6px}
  .contact{position:absolute;left:19px;top:512px;width:160px}
  .contact-line{display:flex;gap:6px;align-items:flex-start;font-size:9px;font-weight:600;margin-bottom:4px;line-height:1.25}
  .contact-line.phone{font-size:12px;font-weight:700}
  .contact-line svg{flex:none;margin-top:1px}
  .divider{position:absolute;left:183px;top:526px;width:1px;height:70px;background:rgba(255,255,255,.45)}
  .backup{position:absolute;left:207px;top:529px;width:214px;font-size:8.4px;line-height:1.45}
  .dots{display:flex;gap:4px;margin-top:8px}
  .dots span{width:9px;height:9px;border-radius:50%;border:1px solid var(--white)}
  .badge{position:absolute;left:706px;top:297px;width:128px;height:128px;border-radius:50%;background:var(--white);display:flex;align-items:center;justify-content:center}
  .badge span{font-weight:700;font-size:16px;color:var(--navy);text-align:center;line-height:1.1}
  .pitch{position:absolute;left:451px;top:466px;width:400px}
  .pitch-kicker{font-size:20px;font-weight:400;line-height:1.2}
  .pitch-title{font-size:29px;font-weight:800;line-height:1.15;margin-bottom:8px}
  .pitch-title u{text-decoration-thickness:2px;text-underline-offset:4px}
  .pitch p{font-size:8.2px;line-height:1.45}
  .pitch-url{display:flex;align-items:center;gap:8px;margin-top:10px;font-size:9.5px;font-weight:600}
  .pitch-url::after{content:"";flex:1;height:1px;background:rgba(255,255,255,.6)}
</style>
</head>
<body>
  <article class="spread">
    <svg class="spread-art" viewBox="0 0 860 606">
      <defs>
        <linearGradient id="photo-tone" x1="0" y1="0" x2="1" y2="1">
          <stop offset="0" stop-color="#8b8782"/>
          <stop offset=".45" stop-color="var(--photo-light)"/>
          <stop offset="1" stop-color="var(--photo-dark)"/>
        </linearGradient>
      </defs>
      <path class="sweep-blue" d="M0,0 V95 C70,300 250,405 455,405 C650,405 790,310 860,150 V0 Z" fill="var(--sky)"/>
      <path class="sweep-white" d="M0,0 V70 C75,282 255,388 455,388 C645,388 785,292 860,128 V0 Z" fill="var(--white)"/>
      <path class="photo-area" d="M30,0 C60,230 250,374 455,374 C640,374 780,282 860,110 V0 Z" fill="url(#photo-tone)" role="img" aria-label="Photo of a bright modern dental treatment room with patient chair and window"/>
    </svg>
    <div class="fold"></div>

    <div class="brand-name">Byte Harbor</div>

    <section class="about">
      <h2 class="section-title">About Us</h2>
      <p>Byte Harbor offers a proven expertise in Dental Practices. We have trained engineers that specialize in Dental practice management solutions.</p>
      <p>We can handle supporting your Practice Management Software to installing IOCs, Remote &amp; Sensors, Pano's, X-rays, scanners, pen pads, and more. Being familiar with Digital technology and how your practice runs we are able to predict and plan for your growth by providing the correct configurations the first time and implementing the proper storage solutions you will require.<br>We know Dental!</p>
    </section>

    <section class="contact">
      <h2 class="section-title">Get In Touch</h2>
      <div class="contact-line">
        <svg width="8" height="11" viewBox="0 0 8 11"><path d="M4 0a4 4 0 0 0-4 4c0 3 4 7 4 7s4-4 4-7a4 4 0 0 0-4-4zm0 5.6A1.6 1.6 0 1 1 4 2.4a1.6 1.6 0 0 1 0 3.2z" fill="#fff"/></svg>
        <span>48 Maple Grove Ave Riverton,<br>MO 65000</span>
      </div>
      <div class="contact-line phone">
        <svg width="10" height="10" viewBox="0 0 10 10"><path d="M2 0l2 2.4-1.2 1.2a6 6 0 0 0 3.6 3.6L7.6 6 10 8l-1.4 1.8C4.5 10 0 5.5.2 1.4z" fill="#fff"/></svg>
        <span>417-555-0182</span>
      </div>
      <div class="contact-line">
        <svg width="9" height="9" viewBox="0 0 10 10"><circle cx="5" cy="5" r="4.3" fill="none" stroke="#fff" stroke-width="1.2"/><path d="M.7 5h8.6M5 .7c-2 2.5-2 6.1 0 8.6M5 .7c2 2.5 2 6.1 0 8.6" fill="none" stroke="#fff" stroke-width=".8"/></svg>
        <span>www.byteharbor-it.com</span>
      </div>
    </section>

    <div class="divider"></div>
    <section class="backup">
      <p>Get started today at <strong>www.toothsafe-backup.com</strong> We don't charge anything until we have confirmation that your Data has been successfully backed up on our encrypted servers.</p>
      <div class="dots"><span></span><span></span><span></span><span></span><span></span><span></span></div>
    </section>

    <div class="badge"><span>Byte<br>Harbor</span></div>

    <section class="pitch">
      <div class="pitch-kicker">READY TO MAKE YOUR</div>
      <h1 class="pitch-title"><u>TECH</u>NOLOGY WORK?</h1>
      <p>Byte Harbor provide Managed IT Services and Sales for all Businesses. We currently support Missouri, Kansas, Arkansas and Oklahoma. Byte Harbor stands out uniquely with our Managed IT clients because of our commitment to not only provide Proactive Management and Support but also to manage Security and Compliance requirements for our client's Network Infrastructure.</p>
      <div class="pitch-url">www.byteharbor-it.com</div>
    </section>
  </article>
</body>
</html>
```